Zielgruppe
Ich bin freie Rednerin. Ich brauche nun einen Flyer für Beerdigungsunternehmen.
Aufgabenstellung
Flyer 4-seitig, quadratisch, 15x15 cm, aufgeklappt 15x30 cm
Bilder von mir lade ich hoch, es reicht aber wenn eines verwendet wird ;)
Ein neutrales Bild mit Thema Trauer kann noch vorgeschlagen werden (nicht zu pathetisch, eher ein Steg der auf einen See hinausführt oder so)
Schriftarten: MyriadPro, Satisfaction

```html
<!DOCTYPE html>
<html lang="de">
<head>
<meta charset="utf-8">
<title>Flyer Trauerrednerin – Innenseiten</title>
<link href="https://fonts.googleapis.com/css2?family=Source+Sans+3:wght@400;600;700&display=swap" rel="stylesheet">
<style>
  :root{
    --red:#c8161d;
    --ink:#2b2b2b;
    --paper:#ffffff;
    --frame:#e7b9bb;
    --soft-line:rgba(190,190,190,.55);
    --photo-light:#f4f3ec;
    --photo-mid:#c9d2b4;
    --photo-deep:#7d8c6a;
  }
  *{box-sizing:border-box;margin:0;padding:0}
  html,body{width:1200px;height:600px;overflow:hidden;background:var(--paper)}
  body{font-family:"Source Sans 3",sans-serif;color:var(--ink);font-size:12.3px;line-height:17.4px}
  .spread{position:relative;width:1200px;height:600px}
  .panel{position:absolute;top:0;width:600px;height:600px;overflow:hidden}
  .panel--left{left:0}
  .panel--right{left:600px;background:var(--paper)}

  .portrait{position:absolute;inset:0;
    background:
      radial-gradient(ellipse 170px 300px at 455px 360px, rgba(60,72,80,.55), rgba(60,72,80,0) 70%),
      radial-gradient(ellipse 260px 220px at 520px 80px, rgba(120,140,90,.55), rgba(120,140,90,0) 70%),
      linear-gradient(90deg, var(--photo-light) 0%, var(--photo-light) 38%, var(--photo-mid) 70%, var(--photo-deep) 100%);}
  .portrait-veil{position:absolute;inset:0;
    background:linear-gradient(90deg, rgba(255,255,255,.9) 0%, rgba(255,255,255,.75) 45%, rgba(255,255,255,0) 75%);}
  .panel-frame{position:absolute;left:66px;top:40px;width:494px;height:600px;border:1px solid var(--soft-line);border-bottom:none}

  .content{position:absolute}
  .about{left:80px;top:77px;width:320px}
  h2{color:var(--red);font-weight:700;font-size:14.6px;line-height:18px}
  p{margin-bottom:11px}
  .offer{margin-top:24px}
  .offer-list{list-style:none;margin-top:1px}
  .offer-list li{position:relative;padding-left:12px;margin-bottom:11px;width:200px}
  .offer-list li::before{content:"~";position:absolute;left:0;top:0}

  .text-box{position:absolute;left:40px;top:39px;width:522px;height:522px;border:1px solid var(--frame)}
  .memory-motif{position:absolute;left:190px;top:170px;width:240px;height:390px;border-radius:120px 120px 30px 30px;
    background:radial-gradient(ellipse at center, rgba(0,0,0,.05), rgba(0,0,0,0) 70%)}
  .preparation{left:80px;top:77px;width:440px}
  .ceremony-title{margin-top:4px;margin-bottom:11px}
  .phone-badge{position:absolute;left:406px;top:116px;background:var(--red);color:#fff;font-weight:700;
    font-size:14px;line-height:22px;padding:0 8px;transform:rotate(-4deg);letter-spacing:.3px;white-space:nowrap}
</style>
</head>
<body>
<main class="spread">
  <section class="panel panel--left">
    <div class="portrait" role="img" aria-label="Foto der Rednerin, lächelnd auf einer sonnigen Sommerwiese stehend"></div>
    <div class="portrait-veil"></div>
    <div class="panel-frame"></div>
    <div class="content about">
      <h2>Über mich</h2>
      <p>Mit Leidenschaft beschäftige ich mich mit Menschen und deren Geschichten.</p>
      <p>Als fundiert ausgebildete Rednerin mit dem Zertifikat der Rednerakademie Rheinland, kann ich Ihnen eine würdevolle und sehr persönlich Verabschiedung Ihres geliebten Menschen gestalten. Empathisch und authentisch verbinde ich mich dessen Persönlichkeit um die Einzigartigkeit seines Lebensweges darzustellen.</p>
      <h2 class="offer">Mein Angebot</h2>
      <ul class="offer-list">
        <li>Die Leitung der gesamten Abschieds-Zeremonie</li>
        <li>Ein Vorgespräch zum Ablauf der Trauerfeier</li>
        <li>Die Gestaltung einer persönlichen Trauerrede</li>
        <li>Die Verabschiedung am Grab</li>
        <li>Bis zur Bestattung ständige Erreichbarkeit bei Rückfragen</li>
      </ul>
    </div>
  </section>

  <section class="panel panel--right">
    <div class="text-box"></div>
    <div class="memory-motif" role="img" aria-label="Zarte Linienzeichnung zweier Figuren als Hintergrundmotiv"></div>
    <div class="content preparation">
      <h2>Die Vorbereitung</h2>
      <p>Sie möchten mich kennenlernen? Ich freue mich auf Ihren Anruf, bei welchem wir vorab schon einige Eckdaten besprechen können.</p>
      <p>Oder Sie schauen sich vorab mein Imagevideo an:<br>Scannen Sie dazu den QR-Code auf der Rückseite mit Ihrem mobilen Gerät ab.</p>
      <p>Anschließend vereinbaren wir ein Treffen, das in Ihrer vertrauten Umgebung stattfindet. Gemeinsam besprechen wir den Ablauf der Zeremonie, mögliche Rituale oder weitere Wortbeiträge. Sie erzählen mir aus dem Leben Ihres Verstorbenen, wie er als Mensch war und welche Eigenschaften er hatte.</p>
      <p>Das, was Sie mir anvertrauen, werde ich in die Trauerrede einflechten. Dabei stehen Ihre Wünsche an oberster Stelle!</p>
      <h2 class="ceremony-title">Die Verabschiedungszeremonie</h2>
      <p>Die Beerdigung wird für Sie ein schwerer Tag sein. Ich werde die Zeremonie so gestalten, dass dieser Tag nicht noch schwerer für Sie wird. Ich möchte Ihnen zur Seite stehen, und Ihnen den Rücken stärken.</p>
      <p>Aus Ihren Informationen verfasse ich eine ganz persönliche Trauerrede, welche den Verstorbenen nochmal ganz intensiv in unsere Erinnerung ruft. Dabei feiern wir vor allem das Leben Ihres Angehörigen. Wir wollen dankbar zurückschauen und die schönen Momente vor Augen führen. Dabei verzichte ich auf jeden Pathos und eine aufgesetzte Sprechweisen. Es ist das letzte, was öffentlich über diesen Menschen gesagt wird. Mir ist sehr bewusst, dass dies mit größter Behutsamkeit und Wertschätzung geschehen muss.</p>
    </div>
    <div class="phone-badge">0160 – 55 81 92 7</div>
  </section>
</main>
</body>
</html>
```